California Cannabis Pre Roll Joint Company needs package graphic design

We are looking for a package graphic design for a shrink sleeve for a small tube style package. This package will hold a 1gr pre rolled cannabis joint. Imagine two chapsticks on top of each other. We have the templates for the sleeves. We have five varieties. Lantern KB, Marbled Hazelnut Cloud Tart, Tidal KX and Amber Drift. We would like to have one layout with a similar background but with individual variety bubbly cartoon style fonts.. We have some other ideas as well we can pass along. We have brand logos and emblems we will forward.

Colors
e557a0
b768aa
a64599
9bcb3c
add136
fbee3f
f37122
f68e4d
0455a3

Requirements
Must have
• we have a compliance panel we must work into the desings

```html
<!DOCTYPE html>
<html lang="en">
<head>
<meta charset="utf-8">
<title>Kestrel Grown Pre-Roll Sleeves</title>
<link href="https://fonts.googleapis.com/css2?family=Oswald:wght@400;500&family=Shrikhand&display=swap" rel="stylesheet">
<style>
  :root{
    --stage:#8d8d8d;
    --ink:#111;
    --paper:#fff;
    --green-a:#3f9e2c; --green-b:#add136;
    --red-a:#ef2a1c; --red-b:#fdb02a;
    --purple-a:#7d1a86; --purple-b:#e51f7d;
    --orange-a:#f37122; --orange-b:#fbb43f;
    --blue-a:#4aa6d6; --blue-b:#3fe0d8; --navy:#1c1a78;
    --pink-a:#e0207a; --pink-b:#f05aa8;
  }
  *{box-sizing:border-box;margin:0;padding:0}
  html,body{width:1166px;height:1200px;overflow:hidden}
  body{background:radial-gradient(circle at 50% 45%,#c9c9c9,var(--stage));position:relative;font-family:"Oswald",sans-serif}
  .sleeve{position:absolute;width:471px;height:310px;background:var(--paper);border:1px solid var(--ink);overflow:hidden}
  .sleeve .band{position:absolute;inset:0;width:100%;height:100%}
  .brand{position:absolute;top:14px;left:0;width:100%;display:flex;justify-content:center;align-items:center;gap:5px}
  .brand .dot{width:12px;height:12px;border-radius:50%;background:var(--mark)}
  .brand span{font-family:"Oswald",sans-serif;font-weight:500;font-size:11px;letter-spacing:1px;color:var(--mark);text-transform:uppercase}
  .art{position:absolute;left:60px;top:62px;width:340px;height:140px;border-radius:50%;opacity:.55;filter:blur(6px)}
  .title{position:absolute;left:40px;width:370px;text-align:center;font-family:"Shrikhand",cursive;color:var(--title);line-height:.95;-webkit-text-stroke:1.5px #2a1020;text-shadow:3px 3px 0 var(--title-shade)}
  .pill{position:absolute;left:146px;top:199px;width:178px;height:23px;border-radius:6px;background:#1a1a1a;color:var(--pill);font-size:12.5px;font-weight:400;display:flex;align-items:center;justify-content:center;letter-spacing:.2px}
  .copy{position:absolute;left:94px;top:229px;width:320px;font-size:6.6px;line-height:1.32;color:#fff;font-weight:400}
  .warning{position:absolute;left:30px;top:218px;width:52px;height:48px}
  .compliance{position:absolute;left:414px;top:58px;width:35px;height:220px;background:#fff;border:1.5px solid var(--ink)}
  .col-l{left:85px}.col-r{left:618px}
  .row-1{top:88px}.row-2{top:440px}.row-3{top:792px}
</style>
</head>
<body>

<svg width="0" height="0" style="position:absolute">
  <defs>
    <linearGradient id="g-green" x1="0" x2="1"><stop offset="0" stop-color="var(--green-a)"/><stop offset=".55" stop-color="var(--green-b)"/><stop offset="1" stop-color="var(--green-a)"/></linearGradient>
    <linearGradient id="g-red" x1="0" x2="1"><stop offset="0" stop-color="var(--red-a)"/><stop offset=".5" stop-color="var(--red-b)"/><stop offset="1" stop-color="var(--red-a)"/></linearGradient>
    <linearGradient id="g-purple" x1="0" x2="1"><stop offset="0" stop-color="var(--purple-a)"/><stop offset=".6" stop-color="var(--purple-b)"/><stop offset="1" stop-color="var(--purple-a)"/></linearGradient>
    <linearGradient id="g-orange" x1="0" x2="1"><stop offset="0" stop-color="var(--orange-a)"/><stop offset=".5" stop-color="var(--orange-b)"/><stop offset="1" stop-color="var(--orange-a)"/></linearGradient>
    <linearGradient id="g-blue" x1="0" x2="1"><stop offset="0" stop-color="var(--blue-a)"/><stop offset=".55" stop-color="var(--blue-b)"/><stop offset="1" stop-color="var(--blue-a)"/></linearGradient>
    <linearGradient id="g-pink" x1="0" x2="1"><stop offset="0" stop-color="var(--pink-a)"/><stop offset=".55" stop-color="var(--pink-b)"/><stop offset="1" stop-color="var(--pink-a)"/></linearGradient>
    <symbol id="warn" viewBox="0 0 52 48"><path d="M26 3 L49 44 L3 44 Z" fill="none" stroke="#fff" stroke-width="4" stroke-linejoin="round"/></symbol>
  </defs>
</svg>

<!-- Lantern KB -->
<section class="sleeve col-l row-1" style="--mark:#2f6b3a;--title:#6cc02e;--title-shade:#f4e430;--pill:#fbee3f">
  <svg class="band" viewBox="0 0 471 310" preserveAspectRatio="none"><path d="M0 158Q235 258 471 158V310H0Z" fill="#1f5a22"/><path d="M0 172Q235 272 471 172V310H0Z" fill="url(#g-green)"/></svg>
  <div class="brand"><i class="dot"></i><span>Kestrel Grown</span></div>
  <div class="art" role="img" aria-label="Coiled cobra illustration with yellow and pink paint splashes" style="background:radial-gradient(ellipse,#e83aa0,#fbee3f 60%,transparent 75%)"></div>
  <div class="title" style="top:112px;font-size:44px">Lantern KB</div>
  <div class="pill">1.0 GRAM /0.035 OUNCE PRE-ROLL</div>
  <svg class="warning"><use href="#warn"/></svg>
  <p class="copy">Lorem ipsum dolor sit amet, consectetuer adipiscing elit, sed diam nonummy nibh euismod tincidunt ut laoreet dolore magna aliquam erat volutpat. Ut wisi enim ad minim veniam, quis nostrud exerci tation ullamcorper suscipit lobortis nisl ut aliquip ex ea commodo consequat. Duis autem vel eum iriure dolor in hendrerit in vulputate velit esse molestie consequat, vel illum dolore eu feugiat nulla facilisis at vero eros et accumsan et iusto odio dignissim qui blandit praesent luptatum zzril delenit augue duis dolore te feugait nulla facilisi.</p>
  <div class="compliance"></div>
</section>

<!-- Tidal KX -->
<section class="sleeve col-r row-1" style="--mark:#8a1c1c;--title:#fbd22a;--title-shade:#e8301c;--pill:#f68e4d">
  <svg class="band" viewBox="0 0 471 310" preserveAspectRatio="none"><path d="M0 158Q235 258 471 158V310H0Z" fill="#9a1a10"/><path d="M0 172Q235 272 471 172V310H0Z" fill="url(#g-red)"/></svg>
  <div class="brand"><i class="dot"></i><span>Kestrel Grown</span></div>
  <div class="art" role="img" aria-label="Orange and red flame illustration" style="background:radial-gradient(ellipse,#fbb03b,#f37122 55%,transparent 75%)"></div>
  <div class="title" style="top:112px;font-size:46px">Tidal KX</div>
  <div class="pill">1.0 GRAM /0.035 OUNCE PRE-ROLL</div>
  <svg class="warning"><use href="#warn"/></svg>
  <p class="copy">Lorem ipsum dolor sit amet, consectetuer adipiscing elit, sed diam nonummy nibh euismod tincidunt ut laoreet dolore magna aliquam erat volutpat. Ut wisi enim ad minim veniam, quis nostrud exerci tation ullamcorper suscipit lobortis nisl ut aliquip ex ea commodo consequat. Duis autem vel eum iriure dolor in hendrerit in vulputate velit esse molestie consequat, vel illum dolore eu feugiat nulla facilisis at vero eros et accumsan et iusto odio dignissim qui blandit praesent luptatum zzril delenit augue duis dolore te feugait nulla facilisi.</p>
  <div class="compliance"></div>
</section>

<!-- Amber Drift -->
<section class="sleeve col-l row-2" style="--mark:#5a2a8a;--title:#e0208a;--title-shade:#7a1a86;--pill:#e557a0">
  <svg class="band" viewBox="0 0 471 310" preserveAspectRatio="none"><path d="M0 158Q235 258 471 158V310H0Z" fill="#4a1a7a"/><path d="M0 172Q235 272 471 172V310H0Z" fill="url(#g-purple)"/></svg>
  <div class="brand"><i class="dot"></i><span>Kestrel Grown</span></div>
  <div class="art" role="img" aria-label="Comic burst with boxing glove illustration" style="background:radial-gradient(ellipse,#e6f03a,#f4ee5a 50%,transparent 72%)"></div>
  <div class="title" style="top:110px;font-size:46px">Amber Drift</div>
  <div class="pill">1.0 GRAM /0.035 OUNCE PRE-ROLL</div>
  <svg class="warning"><use href="#warn"/></svg>
  <p class="copy">Lorem ipsum dolor sit amet, consectetuer adipiscing elit, sed diam nonummy nibh euismod tincidunt ut laoreet dolore magna aliquam erat volutpat. Ut wisi enim ad minim veniam, quis nostrud exerci tation ullamcorper suscipit lobortis nisl ut aliquip ex ea commodo consequat. Duis autem vel eum iriure dolor in hendrerit in vulputate velit esse molestie consequat, vel illum dolore eu feugiat nulla facilisis at vero eros et accumsan et iusto odio dignissim qui blandit praesent luptatum zzril delenit augue duis dolore te feugait nulla facilisi.</p>
  <div class="compliance"></div>
</section>

<!-- Marbled Hazelnut Cloud Tart -->
<section class="sleeve col-r row-2" style="--mark:#c4261c;--title:#fbb43f;--title-shade:#d84a10;--pill:#fbee3f">
  <svg class="band" viewBox="0 0 471 310" preserveAspectRatio="none"><path d="M0 158Q235 258 471 158V310H0Z" fill="#e8401a"/><path d="M0 172Q235 272 471 172V310H0Z" fill="url(#g-orange)"/></svg>
  <div class="brand"><i class="dot"></i><span>Kestrel Grown</span></div>
  <div class="art" role="img" aria-label="Pineapple with sunglasses and green paint splashes" style="background:radial-gradient(ellipse,#9bcb3c,#f4d34a 55%,transparent 75%)"></div>
  <div class="title" style="top:96px;font-size:31px">Marbled Hazelnut<br>Cloud Tart</div>
  <div class="pill">1.0 GRAM /0.035 OUNCE PRE-ROLL</div>
  <svg class="warning"><use href="#warn"/></svg>
  <p class="copy">Lorem ipsum dolor sit amet, consectetuer adipiscing elit, sed diam nonummy nibh euismod tincidunt ut laoreet dolore magna aliquam erat volutpat. Ut wisi enim ad minim veniam, quis nostrud exerci tation ullamcorper suscipit lobortis nisl ut aliquip ex ea commodo consequat. Duis autem vel eum iriure dolor in hendrerit in vulputate velit esse molestie consequat, vel illum dolore eu feugiat nulla facilisis at vero eros et accumsan et iusto odio dignissim qui blandit praesent luptatum zzril delenit augue duis dolore te feugait nulla facilisi.</p>
  <div class="compliance"></div>
</section>

<!-- Glacier Mint -->
<section class="sleeve col-l row-3" style="--mark:#1c1a78;--title:#3a86d0;--title-shade:#1c1a78;--pill:#3fe0d8">
  <svg class="band" viewBox="0 0 471 310" preserveAspectRatio="none"><path d="M0 158Q235 258 471 158V310H0Z" fill="var(--navy)"/><path d="M0 172Q235 272 471 172V310H0Z" fill="url(#g-blue)"/></svg>
  <div class="brand"><i class="dot"></i><span>Kestrel Grown</span></div>
  <div class="art" role="img" aria-label="Blue ice cubes and water splash illustration" style="background:radial-gradient(ellipse,#4ab8f0,#a8def2 55%,transparent 75%)"></div>
  <div class="title" style="top:112px;font-size:44px">Glacier Mint</div>
  <div class="pill">1.0 GRAM /0.035 OUNCE PRE-ROLL</div>
  <svg class="warning"><use href="#warn"/></svg>
  <p class="copy">Lorem ipsum dolor sit amet, consectetuer adipiscing elit, sed diam nonummy nibh euismod tincidunt ut laoreet dolore magna aliquam erat volutpat. Ut wisi enim ad minim veniam, quis nostrud exerci tation ullamcorper suscipit lobortis nisl ut aliquip ex ea commodo consequat. Duis autem vel eum iriure dolor in hendrerit in vulputate velit esse molestie consequat, vel illum dolore eu feugiat nulla facilisis at vero eros et accumsan et iusto odio dignissim qui blandit praesent luptatum zzril delenit augue duis dolore te feugait nulla facilisi.</p>
  <div class="compliance"></div>
</section>

<!-- Berry Cloud Pie -->
<section class="sleeve col-r row-3" style="--mark:#b0184a;--title:#f27ab8;--title-shade:#a8124a;--pill:#f05aa8">
  <svg class="band" viewBox="0 0 471 310" preserveAspectRatio="none"><path d="M0 158Q235 258 471 158V310H0Z" fill="#b0184a"/><path d="M0 172Q235 272 471 172V310H0Z" fill="url(#g-pink)"/></svg>
  <div class="brand"><i class="dot"></i><span>Kestrel Grown</span></div>
  <div class="art" role="img" aria-label="Strawberries with cream swirls and pink splashes" style="background:radial-gradient(ellipse,#e83a5a,#f8c090 55%,transparent 75%)"></div>
  <div class="title" style="top:96px;font-size:38px">Berry<br>Cloud Pie</div>
  <div class="pill">1.0 GRAM /0.035 OUNCE PRE-ROLL</div>
  <svg class="warning"><use href="#warn"/></svg>
  <p class="copy">Lorem ipsum dolor sit amet, consectetuer adipiscing elit, sed diam nonummy nibh euismod tincidunt ut laoreet dolore magna aliquam erat volutpat. Ut wisi enim ad minim veniam, quis nostrud exerci tation ullamcorper suscipit lobortis nisl ut aliquip ex ea commodo consequat. Duis autem vel eum iriure dolor in hendrerit in vulputate velit esse molestie consequat, vel illum dolore eu feugiat nulla facilisis at vero eros et accumsan et iusto odio dignissim qui blandit praesent luptatum zzril delenit augue duis dolore te feugait nulla facilisi.</p>
  <div class="compliance"></div>
</section>

</body>
</html>
```